Business Card Design for Telecommunications and IT Solutions company "ORIV"

BC for telecommunications company name "ORIV" with slogan "Telecom & IT Solutions"

should have the full name as above "ORIV" and the slogan
color reqiured black, red (dark) and white

simple, professional, serious, modern design is required

1 side of business card have a full details, contacts and logo
other side have only the logo, website and full company name "ELORIV Company for Telecommunications service & Information Technology LLC"

i have attached the logo and current business card sample and note that the logo was changed not the same in the attached business card

Industry/Entity Type

Telecommunications

Contact Information for Business Card

Full name: Tamir Hudin Al Qarsi
Job title: General Manager
Mobile no: +964xxxxxxxxx
email: tamir@oriv-example.net
full name of the company: ELORIV Company Telecommunications Services & Information Technology LLC.
website: www.oriv-example.net
address: Tulip Dist. 347/6 HarunQadi, Basra, Iraq

Requirements
Must have
• two languages in the same side of business card (English, Arabic) for only the name and title

```html
<!DOCTYPE html>
<html lang="en">
<head>
<meta charset="utf-8">
<title>ORIV – Business Card</title>
<link rel="stylesheet" href="https://fonts.googleapis.com/css2?family=Arimo:wght@400;700&family=Cairo:wght@400;700&display=swap">
<style>
  :root {
    --bg: #ecebe8;
    --white: #ffffff;
    --wine: #8e2022;
    --wine-light: #a8302f;
    --accent-red: #e0423c;
    --ink: #1f1f1f;
    --grey: #555555;
  }
  * { box-sizing: border-box; margin: 0; padding: 0; }
  html, body {
    width: 1200px; height: 1000px; overflow: hidden;
    background: var(--bg);
    font-family: "Arimo", Arial, sans-serif;
  }
  .stage {
    position: relative; width: 1200px; height: 1000px;
  }
  .card {
    position: absolute; left: 290px;
    width: 620px; height: 354px;
    background: var(--white);
    box-shadow: 0 8px 22px rgba(0,0,0,.18);
    overflow: hidden;
  }
  .card--front { top: 95px; }
  .card--back  { top: 545px; }

  /* Front side */
  .front__brand {
    position: absolute; left: 0; right: 0; top: 22px;
    text-align: center;
  }
  .brand-name {
    font-weight: 700; letter-spacing: 6px;
    line-height: 1;
  }
  .front__brand .brand-name { font-size: 64px; color: var(--ink); }
  .brand-slogan {
    text-transform: uppercase; letter-spacing: 2px;
  }
  .front__brand .brand-slogan { font-size: 13px; color: var(--grey); margin-top: 4px; }
  .front__company { font-size: 14px; color: var(--ink); margin-top: 8px; }
  .front__company-ar {
    font-family: "Cairo", sans-serif; font-size: 13px; color: var(--ink);
    direction: rtl; margin-top: 2px;
  }
  .front__band {
    position: absolute; left: 0; right: 0; top: 186px; height: 126px;
    background: linear-gradient(90deg, var(--wine) 0%, #9c2a2a 100%);
  }
  .person { position: absolute; top: 20px; }
  .person--en { right: 26px; text-align: right; }
  .person--ar {
    left: 26px; top: 64px; text-align: left;
    font-family: "Cairo", sans-serif; direction: rtl;
  }
  .person__name { color: var(--accent-red); font-size: 15px; font-weight: 700; }
  .person__title { color: var(--white); font-size: 14px; }
  .person--ar .person__name { font-size: 16px; line-height: 1.3; }
  .person--ar .person__title { font-size: 14px; line-height: 1.3; }
  .contacts {
    position: absolute; left: 250px; top: 36px;
    color: var(--white); font-size: 15px; letter-spacing: 1px; line-height: 1.75;
  }
  .front__address {
    position: absolute; left: 0; right: 0; bottom: 12px;
    text-align: center; color: var(--wine); font-size: 16px; letter-spacing: 1px;
  }

  /* Back side */
  .back__band {
    position: absolute; left: 0; right: 0; top: 42px; height: 222px;
    background: linear-gradient(90deg, var(--wine) 0%, #a23232 100%);
    text-align: center; color: var(--white);
  }
  .back__band .brand-name { font-size: 92px; margin-top: 22px; }
  .back__band .brand-slogan { font-size: 19px; margin-top: 6px; }
  .back__company { font-size: 14px; font-weight: 700; margin-top: 12px; line-height: 1.3; }
  .back__web {
    position: absolute; left: 0; right: 0; bottom: 34px;
    text-align: center; color: var(--wine); font-size: 18px; letter-spacing: 5px;
  }
</style>
</head>
<body>
<main class="stage">

  <section class="card card--front" aria-label="Business card, contact side">
    <div class="front__brand">
      <div class="brand-name">ORIV</div>
      <div class="brand-slogan">Telecom &amp; IT Solutions</div>
      <div class="front__company">Telecommunications Services &amp; Information Technology LLC</div>
      <div class="front__company-ar" lang="ar">شركة إلوريف لخدمات الإتصالات وتقنية المعلومات المحدودة</div>
    </div>

    <div class="front__band">
      <div class="person person--ar" lang="ar">
        <div class="person__name">تامر هدين القرصي</div>
        <div class="person__title">المدير العام</div>
      </div>
      <div class="contacts">
        <div>+964xxxxxxxxx</div>
        <div>tamir@oriv-example.net</div>
      </div>
      <div class="person person--en">
        <div class="person__name">Tamir Hudin Al Qarsi</div>
        <div class="person__title">General Manager</div>
      </div>
    </div>

    <div class="front__address">Tulip Dist. 347/6 HarunQadi, Basra, Iraq</div>
  </section>

  <section class="card card--back" aria-label="Business card, brand side">
    <div class="back__band">
      <div class="brand-name">ORIV</div>
      <div class="brand-slogan">Telecom &amp; IT Solutions</div>
      <div class="back__company">ELORIV Company for Telecommunications service &amp;<br>Information Technology LLC</div>
    </div>
    <div class="back__web">www.oriv-example.net</div>
  </section>

</main>
</body>
</html>
```